Create a landing page for a new product market combination for an international software company

We are a software company being in the BtoB market for over 20 years. Our product is a software tool that allows for very flexible and versatile cost calculations for companies. We sell to all industries in over 40 countries with 500 clients. We have fairly recently seen a succesfull "competitor" (www.quorvel.com) come up in the niche market of IT costing. This competitor has launched an independent platform with regards to managing IT costs (www.PLXguild.org). In this independent platform standards are set, events are organised and books are written. Since our software can handle all type of costing questions we can en already do play a role in IT costing. We have therefore become a sponsor of the PLX guild. Besides that we came accross the opportunity to buy the URL: www.plxsoftware.com Which we did. We are now looking for a design on that landing page that communicates the fact that the visitor has landed with a company that have in depth knowledge on the PLX subject and provide an effective an affordable tooling for PLX. Currently the difference between the professionalism of our own website (www.brandivex.com) and that of the competitor (www.quorvel.com) and the independent council (www.plxguild.org). is too big.

Target Market(s)

BtB with large IT spend

Number of Pages Required

1 page

Colors

Designer to choose colors to be used in the design.

Requirements
Must have
• A proffessional look and feel
Should not have
• Definetely not too much information and wording

```html
<!DOCTYPE html>
<html lang="en">
<head>
<meta charset="utf-8">
<title>Brandivex – PLX Software</title>
<link href="https://fonts.googleapis.com/css2?family=Lato:wght@400;700;900&family=Open+Sans:wght@400;600;700&display=swap" rel="stylesheet">
<style>
:root{
  --blue:#1f6fb2;
  --blue-dark:#185d96;
  --navy:#0a1a2f;
  --navy-2:#13325a;
  --ink:#222;
  --text:#555;
  --grey-bg:#efefef;
  --footer:#1c1c1c;
  --white:#fff;
}
*{margin:0;padding:0;box-sizing:border-box}
html,body{width:1200px;height:4296px;overflow:hidden}
body{position:relative;font-family:"Open Sans",Arial,sans-serif;color:var(--text);background:var(--white)}
.abs{position:absolute}
a{color:inherit;text-decoration:none}

/* header */
.topbar{left:0;top:0;width:1200px;height:123px;background:var(--blue);z-index:3}
.brand{left:30px;top:40px;display:flex;align-items:center;gap:10px;color:var(--white);font-family:"Lato",sans-serif;font-size:36px;font-weight:400}
.brand .mark{width:14px;height:14px;background:var(--white)}
.contact-top{right:90px;top:26px;display:flex;gap:40px;color:var(--white);font-size:17px}
.contact-top span{display:flex;align-items:center;gap:12px}
.nav{right:90px;top:85px;display:flex;gap:50px;color:var(--white);font-size:17px}

/* hero */
.hero{left:0;top:123px;width:1200px;height:640px;background:radial-gradient(ellipse at 50% 35%,#1b4f83 0%,var(--navy-2) 35%,var(--navy) 75%)}
.hero-title{left:0;top:300px;width:1200px;text-align:center;color:var(--white);font-family:"Lato",sans-serif;font-weight:900;font-size:88px;letter-spacing:1px}
.hero-text{left:300px;top:418px;width:600px;text-align:center;color:#dfe7f1;font-size:17px;line-height:28px}
.btn{display:flex;align-items:center;justify-content:center;gap:12px;font-family:"Lato",sans-serif;font-weight:700;font-size:16px}
.btn-white{background:var(--white);color:var(--blue)}
.btn-outline{border:2px solid var(--white);color:var(--white)}
.btn-blue{background:var(--blue);color:var(--white)}
.hero-btn{left:521px;top:545px;width:157px;height:46px}
.wave{left:0;top:720px;width:1200px;height:70px}
.mouse{left:585px;top:750px;width:30px;height:50px}

/* feature cards */
.feature{top:908px;width:333px;height:278px}
.feature .photo{width:100%;height:100%}
.feature .label{left:22px;top:186px;width:290px;height:66px;background:var(--blue);color:var(--white);font-size:18px;line-height:22px;padding:10px 70px 0 14px}
.feature .go{right:8px;top:8px;width:50px;height:50px;background:var(--white);position:absolute;display:flex;align-items:center;justify-content:center}

/* about */
.about{left:0;top:1309px;width:1200px;height:544px;background:linear-gradient(180deg,#2a78b8,#1d6aa8)}
.section-title{left:0;width:1200px;text-align:center;font-family:"Lato",sans-serif;font-size:38px}
.about .section-title{top:110px;color:var(--white)}
.about-text{left:140px;top:178px;width:920px;text-align:center;color:#e5eef7;font-size:16px;line-height:27px}
.about-text p+p{margin-top:14px}
.about-btn{left:521px;top:372px;width:157px;height:46px}

/* technology */
.tech-title{top:1958px;color:var(--ink)}
.tech-card{top:2090px;width:321px;height:204px;background:var(--white);box-shadow:0 4px 14px rgba(0,0,0,.16);padding:46px 22px 0 22px}
.tech-card h3{font-family:"Lato",sans-serif;font-weight:700;font-size:22px;color:var(--ink);margin-bottom:10px}
.tech-card p{font-size:15px;line-height:25px;color:var(--text);height:100px;overflow:hidden}
.more{font-family:"Lato",sans-serif;font-weight:700;font-size:13px;color:var(--blue);margin-top:12px;display:block}
.diamond{top:-44px;left:22px;width:62px;height:62px;background:var(--blue);transform:rotate(45deg);position:absolute}
.diamond-icon{position:absolute;top:-34px;left:35px;width:36px;height:36px}
.arrow{top:2210px;width:22px;height:36px}

/* who benefits */
.who{left:0;top:2500px;width:1200px;height:579px;background:var(--grey-bg)}
.who-photo{left:89px;top:80px;width:446px;height:419px;background:linear-gradient(160deg,#5d7f97,#28435a 55%,#0e1d2b)}
.who-title{left:601px;top:80px;font-family:"Lato",sans-serif;font-size:38px;color:var(--ink)}
.who-item{left:605px;width:470px}
.who-item h4{display:flex;align-items:center;gap:14px;font-size:18px;font-weight:600;color:var(--blue);margin-bottom:10px}
.who-item p{padding-left:38px;font-size:15px;line-height:26px;color:#444}
.who-btn{left:601px;top:453px;width:147px;height:46px}

/* news */
.news-title{top:3186px;color:var(--ink)}
.news-card{top:3293px;width:426px;height:330px;border:1px solid #cfcfcf;background:var(--white);padding:70px 22px 0 22px}
.news-card h3{font-family:"Lato",sans-serif;font-size:21px;font-weight:400;color:var(--ink);line-height:26px}
.news-card .sub{font-size:14px;color:var(--blue);margin-top:8px}
.news-card p{font-size:14.5px;line-height:25px;color:#444;margin-top:10px}
.news-card .more{margin-top:18px}
.date{top:-34px;left:20px;width:66px;height:64px;background:var(--blue);color:var(--white);text-align:center;font-family:"Lato",sans-serif;font-weight:700;position:absolute}
.date b{display:block;font-size:22px;line-height:30px;padding-top:4px}
.date small{display:block;font-size:15px;border-top:1px solid rgba(255,255,255,.5);margin:0 8px;line-height:24px}
.partner-badge{left:553px;top:3402px;width:92px;height:115px}

/* footer */
.footer{left:0;top:3720px;width:1200px;height:576px;background:var(--footer);color:#ddd}
.footer-wave{left:0;top:3700px;width:1200px;height:110px}
.footer h5{font-family:"Lato",sans-serif;font-weight:400;font-size:24px;color:var(--white)}
.f-links{left:89px;top:212px}
.f-links ul{list-style:none;font-size:14px;line-height:27px;color:#ddd}
.f-col2{left:280px;top:252px}
.f-contact{left:513px;top:212px}
.f-contact p{font-size:14px;line-height:27px;margin-top:14px}
.f-news{left:830px;top:212px}
.f-news p{font-size:14px;margin-top:18px}
.subscribe{left:830px;top:290px;width:278px;height:38px;background:var(--white);border-radius:19px}
.subscribe span{position:absolute;left:18px;top:10px;font-size:13px;color:#777}
.subscribe b{position:absolute;right:4px;top:4px;width:108px;height:30px;border-radius:15px;background:var(--blue);color:var(--white);font-size:13px;font-weight:600;display:flex;align-items:center;justify-content:center}
.social{left:845px;top:368px;display:flex;gap:22px}
.social i{width:14px;height:14px;border-radius:50%;background:#ddd;display:block}
.copy{left:0;top:505px;width:1200px;text-align:center;font-size:13px;color:#ccc}
</style>
</head>
<body>

<header class="abs topbar">
  <div class="abs brand"><span class="mark"></span>Brandivex</div>
  <div class="abs contact-top">
    <span><svg width="18" height="18" viewBox="0 0 24 24" fill="#fff"><path d="M6.6 10.8a15 15 0 006.6 6.6l2.2-2.2c.3-.3.7-.4 1-.2 1.1.4 2.3.6 3.6.6.6 0 1 .4 1 1V20c0 .6-.4 1-1 1A17 17 0 013 4c0-.6.4-1 1-1h3.5c.6 0 1 .4 1 1 0 1.3.2 2.5.6 3.6.1.3 0 .7-.2 1z"/></svg>+31 (0)20 555 0142</span>
    <span><svg width="18" height="18" viewBox="0 0 24 24" fill="#fff"><path d="M3 5h18v14H3z M4 6l8 6 8-6" stroke="#1f6fb2" stroke-width="1.5"/></svg>info@brandivex.com</span>
  </div>
  <nav class="abs nav"><a>Home</a><a>Product</a><a>Markets</a><a>Company</a><a>Partners</a><a>Events</a><a>Support</a><a>Contact</a></nav>
</header>

<section class="abs hero" role="img" aria-label="Dark blue network of connected points in space"></section>
<h1 class="abs hero-title">BRANDIVEX</h1>
<p class="abs hero-text">We are a software company being in the BtoB market for over 20 years. Our product is a software tool that allows for very flexible and versatile cost calculations for companies. We sell to all industries in over 40 countries with 500 clients</p>
<a class="abs btn btn-white hero-btn">READ MORE <svg width="8" height="12" viewBox="0 0 8 12"><path d="M1 1l5 5-5 5" stroke="#1f6fb2" stroke-width="2" fill="none"/></svg></a>
<svg class="abs wave" viewBox="0 0 1200 70" preserveAspectRatio="none"><path d="M0 40 C300 40 450 70 600 70 C750 70 900 40 1200 40 V70 H0Z" fill="#fff"/></svg>
<svg class="abs mouse" viewBox="0 0 30 50"><rect x="2" y="2" width="26" height="44" rx="13" fill="#fff" stroke="#222" stroke-width="2"/><rect x="13" y="10" width="4" height="12" rx="2" fill="#222"/></svg>

<article class="abs feature" style="left:89px">
  <div class="photo" role="img" aria-label="Businesswoman presenting at a whiteboard" style="background:linear-gradient(135deg,#e9e9e9,#9aa4ad 60%,#3b3f45)"></div>
  <div class="abs label">Foster a Business Culture in IT<span class="go"><svg width="12" height="20" viewBox="0 0 12 20"><path d="M2 2l8 8-8 8" stroke="#1f6fb2" stroke-width="2.5" fill="none"/></svg></span></div>
</article>
<article class="abs feature" style="left:432px">
  <div class="photo" role="img" aria-label="Business team meeting around a table" style="background:linear-gradient(135deg,#6e7e52,#4a4a3a 55%,#2b2a26)"></div>
  <div class="abs label">Enable the right business conversations<span class="go"><svg width="12" height="20" viewBox="0 0 12 20"><path d="M2 2l8 8-8 8" stroke="#1f6fb2" stroke-width="2.5" fill="none"/></svg></span></div>
</article>
<article class="abs feature" style="left:776px">
  <div class="photo" role="img" aria-label="Rising blue bar chart with a blurred person" style="background:linear-gradient(135deg,#f3f3f3,#c5d6e6 55%,#3f8ac9)"></div>
  <div class="abs label">Develop Sound Fiscal Disciplines<span class="go"><svg width="12" height="20" viewBox="0 0 12 20"><path d="M2 2l8 8-8 8" stroke="#1f6fb2" stroke-width="2.5" fill="none"/></svg></span></div>
</article>

<section class="abs about" role="img" aria-label="Blue tinted business background">
  <h2 class="abs section-title">About Us</h2>
  <div class="abs about-text">
    <p>Lorem ipsum dolor sit amet, consectetur adipiscing elit, sed do eiusmod tempor incididunt ut labore et dolore magna aliqua. Ut enim ad minim veniam, quis nostrud exercitation ullamco laboris nisi ut aliquip ex ea commodo consequat.</p>
    <p>ed ut perspiciatis unde omnis iste natus error sit voluptatem accusantium doloremque laudantium, totam rem aperiam, eaque ipsa quae ab illo inventore veritatis et quasi architecto beatae vitae dicta sunt explicabo. Nemo enim ipsam voluptatem quia voluptas sit aspernatur aut odit aut fugit, sed quia consequuntur magni dolor</p>
  </div>
  <a class="abs btn btn-outline about-btn">READ MORE <svg width="8" height="12" viewBox="0 0 8 12"><path d="M1 1l5 5-5 5" stroke="#fff" stroke-width="2" fill="none"/></svg></a>
</section>

<h2 class="abs section-title tech-title">Technology</h2>
<svg class="abs arrow" style="left:32px" viewBox="0 0 22 36"><path d="M18 3L5 18l13 15" stroke="#333" stroke-width="5" fill="none"/></svg>
<svg class="abs arrow" style="left:1146px" viewBox="0 0 22 36"><path d="M4 3l13 15L4 33" stroke="#333" stroke-width="5" fill="none"/></svg>

<article class="abs tech-card" style="left:95px">
  <span class="diamond"></span>
  <svg class="diamond-icon" viewBox="0 0 36 36" fill="#fff"><circle cx="12" cy="12" r="5"/><circle cx="24" cy="12" r="5"/><path d="M3 28c0-6 4-9 9-9s9 3 9 9z M16 28c0-6 4-9 9-9s8 3 8 9z"/></svg>
  <h3>POSITION FOR VALUE</h3>
  <p>Define what you deliver in terms of business capabilities that are Understood and valued by your business unit partners, so you can plan with them</p>
  <a class="more">READ MORE »</a>
</article>
<article class="abs tech-card" style="left:441px">
  <span class="diamond"></span>
  <svg class="diamond-icon" viewBox="0 0 36 36"><path d="M5 30h26 M5 30V6" stroke="#fff" stroke-width="3" fill="none"/><path d="M8 24l8-8 5 5 9-10" stroke="#fff" stroke-width="3" fill="none"/></svg>
  <h3>CONTINUOUSLY IMPROVE</h3>
  <p>Execute a strategic roadmap for PLX maturity by integrating PLX into your day-to-day processes and thinking, so that PLX drives every value</p>
  <a class="more">READ MORE »</a>
</article>
<article class="abs tech-card" style="left:788px">
  <span class="diamond"></span>
  <svg class="diamond-icon" viewBox="0 0 36 36"><path d="M28 14a11 11 0 00-20-3 M8 22a11 11 0 0020 3" stroke="#fff" stroke-width="3.5" fill="none"/><path d="M29 5v10h-10z M7 31V21h10z" fill="#fff"/></svg>
  <h3>CREATE TRANSPARENCY</h3>
  <p>Translate your spending, consumption, and capacity into meaningful perspectives for technology and business leaders alike</p>
  <a class="more">READ MORE »</a>
</article>

<section class="abs who">
  <div class="abs who-photo" role="img" aria-label="Person standing before large screens of data in a dark office"></div>
  <h2 class="abs who-title">Who benefits from PLX?</h2>
  <div class="abs who-item" style="top:150px">
    <h4><svg width="16" height="14" viewBox="0 0 16 14"><path d="M1 7l5 5 9-11" stroke="#1f6fb2" stroke-width="3" fill="none"/></svg>IT Leaders</h4>
    <p>"PLX brings business translation so you and your people can quickly decide on trade-offs and new investments to improve competitiveness, customer engagement, and the bottom line." Dana Whitlow, Global CTO, Norvane Group</p>
  </div>
  <div class="abs who-item" style="top:305px">
    <h4><svg width="16" height="14" viewBox="0 0 16 14"><path d="M1 7l5 5 9-11" stroke="#1f6fb2" stroke-width="3" fill="none"/></svg>Business Unit Executives</h4>
    <p>"IT has shifted from being an order taker to an originator of ideas to win in the marketplace." Paul Verhoek, VP Information Technology, Castrel Energy</p>
  </div>
  <a class="abs btn btn-blue who-btn">READ MORE <svg width="8" height="12" viewBox="0 0 8 12"><path d="M1 1l5 5-5 5" stroke="#fff" stroke-width="2" fill="none"/></svg></a>
</section>

<h2 class="abs section-title news-title">News</h2>
<article class="abs news-card" style="left:92px">
  <div class="date"><b>25</b><small>FEB</small></div>
  <h3>Brandivex PLX Cost model</h3>
  <p>Today, CIO's face increased pressure to improve quality, security and availability of IT products where they also have to manage IT costs. With our PLX Based Cost Transparency Model Brandivex provides an analytical tool to support CIO's in their Cost-performance decisions.</p>
  <a class="more">READ MORE</a>
</article>
<svg class="abs partner-badge" role="img" aria-label="Partner badge" viewBox="0 0 92 115"><rect x="6" y="4" width="80" height="60" fill="#e5611b"/><rect x="6" y="72" width="80" height="38" fill="#dcdcdc"/></svg>
<article class="abs news-card" style="left:682px">
  <div class="date"><b>25</b><small>FEB</small></div>
  <h3>Cost Management Training Course Vietnam</h3>
  <div class="sub">Where Theory and Practice meet</div>
  <p>In a joint venture with Lumera Advisory Vietnam, Brandivex has organized three cost management workshops in Hanoi and Ho Chi Minh City, Vietnam. 85 participants from 30 companies attended the (paid) workshops to learn more</p>
  <a class="more">READ MORE</a>
</article>

<footer class="abs footer">
  <div class="abs f-links"><h5>Links</h5>
    <ul style="margin-top:18px"><li>Home</li><li>Product</li><li>Markets</li><li>Company</li><li>Partners</li><li>Events</li><li>Support</li><li>Contact</li></ul>
  </div>
  <ul class="abs f-col2" style="list-style:none;font-size:14px;line-height:27px"><li>Terms &amp; Services</li><li>Privacy Policy</li><li>Faq</li></ul>
  <div class="abs f-contact"><h5>Contact Us</h5>
    <p>Brandivex BV Lindenkade 12<br>3511 KP Utrecht The Netherlands<br>Tel: +31 (0)20 555 0140<br>Helpdesk: +31 (0)20 555 0142<br>Fax: +31 (0)20 555 0199</p>
  </div>
  <div class="abs f-news"><h5>Newsletter</h5><p>Subscribe Our Newsletter For More Info</p></div>
  <div class="abs subscribe"><span>Email Address</span><b>SUBSCRIBE</b></div>
  <div class="abs social"><i></i><i></i><i></i><i></i><i></i></div>
  <p class="abs copy">© Copyright 2019 The Company name. All Rights Reserved.</p>
</footer>
<svg class="abs footer-wave" viewBox="0 0 1200 110" preserveAspectRatio="none"><path d="M0 0H1200V20 C900 20 750 75 600 75 C450 75 300 20 0 20Z" fill="#fff"/></svg>
<svg class="abs mouse" style="top:3722px" viewBox="0 0 30 50"><rect x="2" y="2" width="26" height="44" rx="13" fill="#fff" stroke="#222" stroke-width="2"/><rect x="13" y="10" width="4" height="12" rx="2" fill="#222"/></svg>

</body>
</html>
```